Professional Lawn Treatment flyer (double sided) needed for established gardening company

We are an established and trusted gardening company in Swindon, UK, and are about to launch a new Lawn Treatment Service. This will be marketed to both existing and new customers and needs to reflect our current professional image. The flyer will need to be double-sided, portrait orientation and correctly sized so to be printed on A5.

If you look on our website www.tavistrowgardening.co.uk, you will see our colours are purple and green. We would like you to use these exact shades of purple and green in your design.

As part of the design, we will need you to put together an infographic table to show our packages. I have attached a spreadsheet which explains these packages but I will need you to create a visually appealing table that fits in with the overall design of the flyer. I don't want you to simply cut and paste my basic table into the design.

In terms of what needs to be included, I have tried to be as specific as possible here but please feel free to message me if you need any further information or clarification.

FRONT SIDE:
The title of our service is:
Expert Lawn Treatment Service

Our strapline will need to be included somewhere:
"Lawn care by your local gardening expert"

The front side of the flyer will need to contain our logo - different versions of which can be found within my dropbox folder here...

https://www.sharebinnu.co.uk/sh/k7qd21mzplax/QRT8xWbnNeLu4Pa-ZxYyhKcLo?dl=0

The front side will need to contain a main image (although feel free to add more if you have anything suitable). I have included a picture in the dropbox folder titled "Front side image" which we would like used. I've also included in the folder an adobe image of grass which you may or may not like to use on either front or back.

Somewhere on both the front and back sides, you will need to include our contact details:
01632 960417
www.tavistrowgardening.co.uk/lawncare

The front side should show what treatments we currently have available. These are:

- Lawn Fertilising
- Scarification
- Aeration
- Weed Control
- Moss Control
- Hydration Booster
- PlumeRest
- Turfing & Renovation

"Select a one-off treatment or choose from one of our specially created lawn care packages."

BACK SIDE:
On the back, we will still need our logo and contact details but the image we'd like used should be the one in the dropbox folder titled "Back side image". Again, if you have any other images you feel would also work, then please feel free to add them.

The back side is to contain a bit more information and be a bit 'wordier' and so can you please include the following 2 paragraphs:

"As expert gardeners, we are passionate about horticulture and working to bring out the very best in your garden. When we work in your garden, we look at it and treat it with the same care and attention as if it were our own, before handing it back for you to enjoy. Our passion doesn't end at just trees and shrubs though. Your grass is as much of a living, breathing plant as your shrubs and we therefore utilise our expert horticultural knowledge to ensure your lawn thrives and reaches its fullest potential.

Lawn care isn't just about applying a fertiliser. It's about really understanding your lawn and being able to use extensive knowledge and experience to diagnose and treat issues. It therefore stands to reason that you should employ an expert to bring out the best in your lawn which is why we at Tavistrow Gardening Services have created a superior lawn care service that will keep your lawn looking lush, green and healthy all year round."

I referred at the very top of this brief to the fact we will need an infographic table created to show the different lawn care packages available. You see from the PDF table I created that we have 3 packages; Standard, Enhanced and Premium. Please create a visually appealing table which sets out the differences between our packages and include it on the back page.

Finally, somewhere we would like reference to the other gardening services we do. It's only to be something small as it isn't the main focus of the flyer but we think it would be good to mention what else we do. To re-iterate, it isnt to be big. I still want the main focus to be lawn care but if you could somehow reference that we also do the following services, that would be good. I will leave it to you to decide where on the flyer it fits in best, be it the front or back:

- Lawn mowing
- Shrub pruning
- Hedge trimming
- Weed killing
- Garden clearance & tidy-up
- Planting & design
- Regular Garden Maintenance
- Turfing
- Fencing
- Gutter clearance

I think thats it. I look forward to your designs!
Ps. Don't forget the dropbox folder:

Target Market(s)

Professional men/women aged 25+
Retired aged 65+

Industry/Entity Type

Home And Garden

Font styles to use
Sans Serif

Colors
6b449b
9bcb3c

Requirements
Must have
• Our company colours; purple and green; as per our website www.tavistrowgardening.co.uk. I've selected purple and green on this brief just to highlight the colours needed but please be sure to use the exact shades from our website and NOT the shade of purple and green that were selected on this brief.
• All the wording as explained in the main project brief.
Nice to have
• I want the flyer to be bold, eye-catching and modern.
• We particularly like the font Trebuchet MS for general copy but please feel free to use any other font for bolder, main titles.
Should not have
• We don't want anything gimmicky. No cheesy marketing.
• We only want professional looking designs. With the greatest of respect, if you're just starting out or don't really do design but think you'll use this as practise, please don't waste your or our time. We've previously run contests for other projects where we've had designs submitted that have clearly been done on MS Word and used Clipart and Wordart. That's really not what we are looking for.

```html
<!DOCTYPE html>
<html lang="en">
<head>
<meta charset="utf-8">
<title>Tavistrow Gardening Services – Lawn Treatment Flyer</title>
<link href="https://fonts.googleapis.com/css2?family=Ropa+Sans&family=Signika:wght@300;400;600&display=swap" rel="stylesheet">
<style>
  :root{
    --purple:#7a2a8b;
    --purple-dark:#5f1f6e;
    --green:#45a12e;
    --green-dark:#2f7f22;
    --lime:#a6cf3a;
    --white:#ffffff;
    --paper:#f3f3f1;
    --stage:#e8e5e0;
  }
  *{box-sizing:border-box;margin:0;padding:0}
  html,body{width:1200px;height:818px;overflow:hidden;background:var(--stage)}
  body{position:relative;font-family:"Signika",sans-serif;font-weight:400}
  .flyer{position:absolute;top:83px;width:451px;height:639px;background:var(--white);overflow:hidden;box-shadow:0 4px 14px rgba(0,0,0,.25)}
  .flyer--front{left:118px}
  .flyer--back{left:645px;background:var(--paper)}
  .flyer__art{position:absolute;inset:0}
  .abs{position:absolute}
  .brand{display:flex;align-items:center;gap:8px;font-family:"Ropa Sans",sans-serif;font-size:21px;line-height:21px;color:var(--purple);width:190px}
  .brand__dot{flex:0 0 22px;height:22px;border-radius:50%;background:var(--lime)}
  .title-purple{font-family:"Ropa Sans",sans-serif;font-weight:400;color:var(--purple);font-size:17px;line-height:21px;letter-spacing:.3px}
  .headline{left:0;width:451px;text-align:center;color:var(--white);font-family:"Ropa Sans",sans-serif;font-weight:400}
  .headline--main{top:286px;font-size:27px}
  .headline--sub{top:319px;font-size:22px}
  .services-tab{left:0;top:362px;width:174px;height:27px;background:var(--lime);border-radius:0 14px 14px 0;color:var(--white);font-family:"Ropa Sans",sans-serif;font-size:18px;line-height:27px;padding-left:18px}
  .treatments{left:20px;top:398px;list-style:none;color:var(--white);font-weight:300;font-size:15.5px;line-height:19.3px}
  .treatments li{display:flex;align-items:center;gap:6px}
  .tick{width:10px;height:10px;flex:0 0 10px}
  .other-services{top:382px;list-style:none;color:var(--white);font-weight:300;font-size:10px;line-height:11.7px}
  .other-services--left{left:232px;width:110px}
  .other-services--right{left:345px;width:98px}
  .other-services li{padding-left:7px;text-indent:-7px}
  .other-services li::before{content:"·";display:inline-block;width:7px;text-indent:0}
  .cta{left:234px;top:464px;width:204px;height:85px;background:var(--purple);border-radius:6px;box-shadow:0 3px 5px rgba(0,0,0,.3);color:var(--white);font-style:italic;font-weight:400;font-size:13px;line-height:18.5px;text-align:center;display:flex;align-items:center;justify-content:center}
  .footer{left:0;top:599px;width:451px;height:40px}
  .social{position:absolute;top:9px;width:19px;height:19px;border-radius:50%;background:var(--purple)}
  .contact{position:absolute;left:0;width:451px;text-align:center;color:var(--purple);font-size:13px;line-height:16px;top:4px}
  .contact svg{width:11px;height:11px;vertical-align:-1px;margin-right:2px}
  .packages-title{left:19px;top:232px;font-family:"Ropa Sans",sans-serif;font-weight:400;color:var(--purple);font-size:16.5px}
  .package{left:30px;width:161px;box-shadow:0 3px 4px rgba(0,0,0,.3);border-radius:3px;overflow:hidden}
  .package__head{background:var(--green);color:var(--white);font-weight:300;font-size:9px;text-align:center;height:15px;line-height:15px;text-transform:uppercase}
  .package__list{background:var(--purple);list-style:none;padding:4px 0 6px 18px;color:var(--white);font-weight:300;font-size:9px;line-height:11.7px}
  .package__list li{position:relative}
  .package__list li::before{content:"";position:absolute;left:-10px;top:3px;width:6px;height:6px;border-radius:50%;background:var(--lime)}
  .about-title{left:246px;top:224px;width:192px;text-align:center;font-family:"Ropa Sans",sans-serif;font-weight:400;color:var(--white);font-size:15.5px;line-height:18px}
  .about-copy{left:246px;top:270px;width:192px;color:var(--white);font-family:"Ropa Sans",sans-serif;font-size:9.3px;line-height:10.3px;text-align:justify}
  .about-copy p+p{margin-top:10px}
</style>
</head>
<body>

<section class="flyer flyer--front">
  <svg class="flyer__art" viewBox="0 0 451 639" width="451" height="639">
    <defs>
      <linearGradient id="f-photo" x1="0" y1="0" x2="1" y2="1">
        <stop offset="0" stop-color="#5c8f3a"/><stop offset=".45" stop-color="#7fb548"/><stop offset=".7" stop-color="#c9c2b3"/><stop offset="1" stop-color="#b8b0a1"/>
      </linearGradient>
      <linearGradient id="f-green" x1="0" y1="0" x2="0" y2="1">
        <stop offset="0" stop-color="#3d9a2c"/><stop offset="1" stop-color="#56b236"/>
      </linearGradient>
      <linearGradient id="grass" x1="0" y1="0" x2="0" y2="1">
        <stop offset="0" stop-color="#6ec140"/><stop offset=".5" stop-color="#2f8a22"/><stop offset="1" stop-color="#1f6a18"/>
      </linearGradient>
      <radialGradient id="c-turf"><stop offset="0" stop-color="#6f8a3c"/><stop offset="1" stop-color="#4f6b2a"/></radialGradient>
      <radialGradient id="c-mow"><stop offset="0" stop-color="#5aa63a"/><stop offset="1" stop-color="#3a7c2a"/></radialGradient>
      <radialGradient id="c-hand"><stop offset="0" stop-color="#8cc24f"/><stop offset="1" stop-color="#4a8a30"/></radialGradient>
    </defs>
    <g role="img" aria-label="Photo of a garden lawn with a curving paved path">
      <rect x="0" y="0" width="451" height="270" fill="url(#f-photo)"/>
    </g>
    <path d="M0,0 H226 C232,70 215,150 160,185 C120,208 60,206 0,216 Z" fill="var(--white)"/>
    <path d="M226,0 C232,70 215,150 160,185 C120,208 60,206 0,216" fill="none" stroke="var(--purple)" stroke-width="5"/>
    <path d="M236,0 C242,80 222,160 165,193" fill="none" stroke="var(--lime)" stroke-width="3"/>
    <path d="M0,236 C110,272 270,270 451,236 V639 H0 Z" fill="url(#f-green)"/>
    <path d="M0,236 C110,272 270,270 451,236 L451,222 C270,256 110,258 0,220 Z" fill="var(--lime)"/>
    <path d="M0,224 C110,258 270,258 451,222 L451,205 C270,238 110,242 0,200 Z" fill="var(--purple)"/>
    <g role="img" aria-label="Photo of turf being rolled out">
      <circle cx="228" cy="222" r="35" fill="url(#c-turf)" stroke="var(--lime)" stroke-width="3"/>
    </g>
    <g role="img" aria-label="Photo of a lawn being mowed">
      <circle cx="319" cy="222" r="35" fill="url(#c-mow)" stroke="var(--lime)" stroke-width="3"/>
    </g>
    <g role="img" aria-label="Photo of gloved hands tending grass">
      <circle cx="403" cy="222" r="35" fill="url(#c-hand)" stroke="var(--lime)" stroke-width="3"/>
    </g>
    <g role="img" aria-label="Photo of a strip of grass blades">
      <rect x="0" y="557" width="451" height="42" fill="url(#grass)"/>
    </g>
    <rect x="0" y="597" width="451" height="42" fill="var(--white)"/>
  </svg>

  <div class="abs brand" style="left:19px;top:40px"><span class="brand__dot"></span>Tavistrow Gardening Services</div>
  <h2 class="abs title-purple" style="left:19px;top:106px">EXPERT LAWN<br>TREATMENT SERVICE</h2>

  <h1 class="abs headline headline--main">LAWN CARE</h1>
  <p class="abs headline headline--sub">BY YOUR LOCAL GARDENING EXPERT</p>

  <div class="abs services-tab">OUR SERVICES</div>
  <ul class="abs treatments">
    <li><svg class="tick" viewBox="0 0 10 10"><circle cx="5" cy="5" r="5" fill="#a6cf3a"/><path d="M2.5,5 L4.4,6.8 L7.6,3.4" fill="none" stroke="#3d9a2c" stroke-width="1.4"/></svg>Lawn Fertilising</li>
    <li><svg class="tick" viewBox="0 0 10 10"><circle cx="5" cy="5" r="5" fill="#a6cf3a"/><path d="M2.5,5 L4.4,6.8 L7.6,3.4" fill="none" stroke="#3d9a2c" stroke-width="1.4"/></svg>Scarification</li>
    <li><svg class="tick" viewBox="0 0 10 10"><circle cx="5" cy="5" r="5" fill="#a6cf3a"/><path d="M2.5,5 L4.4,6.8 L7.6,3.4" fill="none" stroke="#3d9a2c" stroke-width="1.4"/></svg>Aeration</li>
    <li><svg class="tick" viewBox="0 0 10 10"><circle cx="5" cy="5" r="5" fill="#a6cf3a"/><path d="M2.5,5 L4.4,6.8 L7.6,3.4" fill="none" stroke="#3d9a2c" stroke-width="1.4"/></svg>Weed Control</li>
    <li><svg class="tick" viewBox="0 0 10 10"><circle cx="5" cy="5" r="5" fill="#a6cf3a"/><path d="M2.5,5 L4.4,6.8 L7.6,3.4" fill="none" stroke="#3d9a2c" stroke-width="1.4"/></svg>Moss Control</li>
    <li><svg class="tick" viewBox="0 0 10 10"><circle cx="5" cy="5" r="5" fill="#a6cf3a"/><path d="M2.5,5 L4.4,6.8 L7.6,3.4" fill="none" stroke="#3d9a2c" stroke-width="1.4"/></svg>Hydration Booster</li>
    <li><svg class="tick" viewBox="0 0 10 10"><circle cx="5" cy="5" r="5" fill="#a6cf3a"/><path d="M2.5,5 L4.4,6.8 L7.6,3.4" fill="none" stroke="#3d9a2c" stroke-width="1.4"/></svg>PlumeRest</li>
    <li><svg class="tick" viewBox="0 0 10 10"><circle cx="5" cy="5" r="5" fill="#a6cf3a"/><path d="M2.5,5 L4.4,6.8 L7.6,3.4" fill="none" stroke="#3d9a2c" stroke-width="1.4"/></svg>Turfing &amp; Renovation</li>
  </ul>

  <ul class="abs other-services other-services--left">
    <li>Lawn mowing</li><li>Shrub pruning</li><li>Hedge trimming</li><li>Weed killing</li><li>Garden clearance<br>&amp; tidy-up</li>
  </ul>
  <ul class="abs other-services other-services--right">
    <li>Planting &amp; design</li><li>Turfing</li><li>Fencing</li><li>Gutter clearance</li><li>Regular Garden<br>Maintenance</li>
  </ul>

  <div class="abs cta"><p>Select a one-off treatment<br>or choose from one of our<br>specially created<br>lawn care packages.</p></div>

  <footer class="abs footer">
    <span class="social" style="left:10px"></span>
    <span class="social" style="left:33px"></span>
    <p class="contact"><svg viewBox="0 0 12 12"><circle cx="6" cy="6" r="5.3" fill="none" stroke="#7a2a8b" stroke-width="1.2"/><path d="M4,3.3 L5,3.3 L5.5,4.8 L4.9,5.3 C5.3,6.2 5.8,6.7 6.7,7.1 L7.2,6.5 L8.7,7 L8.7,8 C6,8.3 3.7,6 4,3.3 Z" fill="#7a2a8b"/></svg>01632 960417<br>www.tavistrowgardening.co.uk/lawncare</p>
  </footer>
</section>

<section class="flyer flyer--back">
  <svg class="flyer__art" viewBox="0 0 451 639" width="451" height="639">
    <defs>
      <linearGradient id="b-photo" x1="0" y1="0" x2="0" y2="1">
        <stop offset="0" stop-color="#4f6b3a"/><stop offset=".35" stop-color="#5fa03a"/><stop offset="1" stop-color="#7cc444"/>
      </linearGradient>
      <linearGradient id="b-panel" x1="0" y1="0" x2="0" y2="1">
        <stop offset="0" stop-color="#3d9a2c"/><stop offset="1" stop-color="#58b437"/>
      </linearGradient>
      <linearGradient id="grass2" x1="0" y1="0" x2="0" y2="1">
        <stop offset="0" stop-color="#6ec140"/><stop offset=".5" stop-color="#2f8a22"/><stop offset="1" stop-color="#1f6a18"/>
      </linearGradient>
      <radialGradient id="c-hedge"><stop offset="0" stop-color="#6a8f45"/><stop offset="1" stop-color="#3f6a2a"/></radialGradient>
      <radialGradient id="c-house"><stop offset="0" stop-color="#9aa27a"/><stop offset="1" stop-color="#4f8a35"/></radialGradient>
    </defs>
    <g role="img" aria-label="Photo of a striped lawn beside a stone path and patio">
      <rect x="0" y="0" width="451" height="200" fill="url(#b-photo)"/>
    </g>
    <path d="M0,0 H156 C162,55 130,98 70,106 C40,110 18,110 0,112 Z" fill="var(--white)"/>
    <path d="M156,0 C162,55 130,98 70,106 C40,110 18,110 0,112" fill="none" stroke="var(--purple)" stroke-width="4"/>
    <path d="M164,0 C170,60 138,106 75,114" fill="none" stroke="var(--lime)" stroke-width="2.5"/>
    <path d="M0,168 C90,215 190,200 270,150 L451,150 V200 L0,220 Z" fill="var(--paper)"/>
    <path d="M0,172 C90,210 180,196 262,150 L262,168 C180,214 90,226 0,196 Z" fill="var(--purple)"/>
    <path d="M0,196 C90,226 180,214 262,168 L262,174 C180,222 90,232 0,203 Z" fill="var(--lime)"/>
    <path d="M256,178 C240,260 230,420 240,597 H451 V205 C400,200 330,200 256,178 Z" fill="url(#b-panel)"/>
    <path d="M256,178 C240,260 230,420 240,597" fill="none" stroke="var(--lime)" stroke-width="5"/>
    <path d="M256,178 C330,200 400,200 451,205 L451,196 C400,192 330,192 258,168 Z" fill="var(--lime)"/>
    <g role="img" aria-label="Photo of a gardener trimming a hedge">
      <circle cx="295" cy="162" r="43" fill="url(#c-hedge)" stroke="var(--lime)" stroke-width="3"/>
    </g>
    <g role="img" aria-label="Photo of a front garden with flower beds">
      <circle cx="397" cy="162" r="43" fill="url(#c-house)" stroke="var(--lime)" stroke-width="3"/>
    </g>
    <g role="img" aria-label="Photo of a strip of grass blades">
      <rect x="0" y="557" width="451" height="42" fill="url(#grass2)"/>
    </g>
    <rect x="0" y="597" width="451" height="42" fill="var(--white)"/>
  </svg>

  <div class="abs brand" style="left:15px;top:30px;width:140px;font-size:18px;line-height:18px"><span class="brand__dot" style="flex-basis:18px;height:18px"></span>Tavistrow Gardening Services</div>

  <h2 class="abs packages-title">LAWN TREATMENT PACKAGES</h2>

  <div class="abs package" style="top:255px">
    <div class="package__head">Standard Package</div>
    <ul class="package__list"><li>Spring Treatment</li><li>Early Summer Treatment</li><li>Late Summer Treatment</li><li>Autumn/Winter Treatment</li></ul>
  </div>
  <div class="abs package" style="top:339px">
    <div class="package__head">Enhanced Package</div>
    <ul class="package__list"><li>Spring Treatment</li><li>Early Summer Treatment</li><li>Late Summer Treatment</li><li>Autumn/Winter Treatment</li><li>Scarification</li><li>Aeration</li></ul>
  </div>
  <div class="abs package" style="top:443px">
    <div class="package__head">Enhanced Package</div>
    <ul class="package__list"><li>Spring Treatment</li><li>Early Summer Treatment</li><li>Late Summer Treatment</li><li>Autumn/Winter Treatment</li><li>Scarification</li><li>Aeration</li><li>PlumeRest Treatment</li><li>Hydration Boost Treatment</li></ul>
  </div>

  <h2 class="abs about-title">EXPERT LAWN<br>TREATMENT SERVICE</h2>
  <div class="abs about-copy">
    <p>As expert gardeners, we are passionate about horticulture and working to bring out the very best in your garden. When we work in your garden, we look at it and treat it with the same care and attention as if it were our own, before handing it back for you to enjoy. Our passion doesn't end at just trees and shrubs though. Your grass is as much of a living, breathing plant as your shrubs and we therefore utilise our expert horticultural knowledge to ensure your lawn thrives and reaches its fullest potential.</p>
    <p>Lawn care isn't just about applying a fertiliser. It's about really understanding your lawn and being able to use extensive knowledge and experience to diagnose and treat issues. It therefore stands to reason that you should employ an expert to bring out the best in your lawn which is why we at Tavistrow Gardening Services have created a superior lawn care service that will keep your lawn looking lush, green and healthy all year round.</p>
  </div>

  <footer class="abs footer">
    <span class="social" style="left:10px"></span>
    <span class="social" style="left:33px"></span>
    <p class="contact"><svg viewBox="0 0 12 12"><circle cx="6" cy="6" r="5.3" fill="none" stroke="#7a2a8b" stroke-width="1.2"/><path d="M4,3.3 L5,3.3 L5.5,4.8 L4.9,5.3 C5.3,6.2 5.8,6.7 6.7,7.1 L7.2,6.5 L8.7,7 L8.7,8 C6,8.3 3.7,6 4,3.3 Z" fill="#7a2a8b"/></svg>01632 960417<br>www.tavistrowgardening.co.uk/lawncare</p>
  </footer>
</section>

</body>
</html>
```